Redesign responsive website and logo for webshop platform

Redesign our applications old website with a new clean, crisp modern looking style that is responsive.

Our application is a cloud based, free ecommerce platform that lets users set up their own webshops within minutes. (Similar to Bramvik https://bramvik.example/l/sell)

Our old website: http://sv.kelporia.example/

I need redesigned HTML + CSS for the following three pages:
* Landing Page:
(Old page: http://sv.kelporia.example/)
I have attached a mockup of a proposed layout/structure for the landing page.
- Pricing comparision/features page
(Old page http://sv.kelporia.example/t/funktioner)
- Generic "article" page:
(Old page http://sv.kelporia.example/d/redigerasida)

The pages must responsive using HTML 5/CSS 3 (I prefer Bootstrap 3 if possible).

I also need a redesign of the logotype.

If you have any questions don't hesitate to ask and we will provide whatever is needed to you.

Logo Text

Kelporia

Coding

Coded - Design and coding required

Number of Pages Required

3 page

Font styles to use
Serif
Sans Serif

```html
<!DOCTYPE html>
<html lang="sv">
<head>
<meta charset="utf-8">
<title>Kelporia – Starta en gratis webshop</title>
<link rel="stylesheet" href="https://fonts.googleapis.com/css2?family=Open+Sans:wght@300;400;600;700&family=Montserrat:wght@700&display=swap">
<style>
:root{
  --blue:#2aa3e0;
  --blue-dark:#1a86cc;
  --blue-light:#7fd0f5;
  --ink:#3a4048;
  --muted:#8a9199;
  --line:#e3e7eb;
  --bg:#ffffff;
  --footer:#2b2d30;
  --footer-text:#9aa0a6;
}
*{box-sizing:border-box;margin:0;padding:0}
html,body{width:1200px;height:2672px;overflow:hidden;background:var(--bg);font-family:"Open Sans",Arial,sans-serif;color:var(--ink)}
a{color:inherit;text-decoration:none}

/* Hero */
.hero{position:relative;height:600px;background:linear-gradient(180deg,#2ea8e3 0%,#1f92d5 100%);color:#fff;overflow:hidden}
.nav{position:absolute;top:28px;left:60px;right:60px;display:flex;align-items:center;justify-content:space-between}
.brand{font-family:"Montserrat",sans-serif;font-weight:700;font-size:26px;letter-spacing:1px}
.menu{display:flex;gap:30px;align-items:center;font-size:13px}
.menu .signup{background:#fff;color:var(--blue);padding:6px 16px;border-radius:3px;font-weight:600}
.hero-copy{position:absolute;left:60px;top:170px;width:440px}
.hero-copy h1{font-weight:300;font-size:40px;line-height:1.15;margin-bottom:18px}
.hero-copy p{font-size:14px;line-height:1.6;opacity:.9;margin-bottom:34px}
.btn-ghost{display:inline-block;border:2px solid #fff;border-radius:30px;padding:12px 30px;font-size:14px;font-weight:600}
.devices{position:absolute;left:590px;top:120px;width:420px;height:330px;border-radius:14px;background:linear-gradient(135deg,#1b2430 0%,#3a4756 55%,#e9eef3 100%)}
.wave{position:absolute;left:0;bottom:0;width:1200px;height:200px}

/* Feature grid */
.features{position:absolute;top:600px;left:0;width:1200px;height:460px;padding:40px 0 0 220px;display:grid;grid-template-columns:430px 430px;column-gap:110px;row-gap:44px}
.feature{display:flex;gap:18px}
.feature svg{flex:0 0 40px;width:40px;height:40px}
.feature h3{font-size:16px;font-weight:600;color:var(--blue);margin-bottom:8px}
.feature p{font-size:12px;line-height:1.6;color:var(--muted)}

/* Funktioner */
.intro{position:absolute;top:1070px;left:0;width:1200px;text-align:center}
.intro h2{font-size:38px;font-weight:300;color:var(--blue);margin-bottom:24px}
.intro p{width:460px;margin:0 auto 16px;font-size:13px;line-height:1.6;color:var(--ink)}

.plans{position:absolute;top:1390px;left:0;width:1200px;display:flex;justify-content:center;gap:95px}
.plan{position:relative;width:300px;height:460px;background:#fff;box-shadow:0 8px 30px rgba(0,0,0,.12);overflow:hidden;padding:40px 34px}
.plan .tag{font-size:10px;font-weight:700;letter-spacing:1px;color:var(--blue)}
.plan .price{font-size:56px;font-weight:300;margin:14px 0 24px;color:var(--ink)}
.plan .price small{font-size:12px;color:var(--blue);margin-left:6px}
.plan ul{list-style:none;font-size:12px;line-height:1.9;color:var(--muted)}
.plan .plan-wave{position:absolute;left:0;bottom:0;width:300px;height:150px}
.plan .buy{position:absolute;left:50%;bottom:40px;transform:translateX(-50%);background:var(--blue-dark);color:#fff;font-size:13px;padding:9px 34px;border-radius:3px;border:1px solid rgba(255,255,255,.5)}

/* Small features */
.small-features{position:absolute;top:1930px;left:170px;width:860px;display:grid;grid-template-columns:repeat(3,1fr);row-gap:70px}
.small{padding:0 30px;border-left:1px solid var(--line)}
.small:nth-child(3n+1){border-left:none;padding-left:0}
.small h4{font-size:14px;font-weight:600;margin-bottom:14px}
.small p{font-size:11px;line-height:1.7;color:var(--muted)}

/* Footer */
.footer{position:absolute;top:2420px;left:0;width:1200px;height:252px;background:var(--footer);color:var(--footer-text);padding:50px 170px 0;display:grid;grid-template-columns:230px 170px 260px 1fr;gap:30px;font-size:11px;line-height:1.7}
.footer .brand{color:#fff;font-size:22px;margin-bottom:10px}
.footer h5{color:#fff;font-size:12px;font-weight:600;margin-bottom:12px}
.footer ul{list-style:none}
.tweet{display:flex;gap:10px;margin-bottom:12px}
.tweet i,.contact i{flex:0 0 8px;width:8px;height:8px;border-radius:50%;background:var(--blue);margin-top:5px}
.contact li{display:flex;gap:10px;margin-bottom:6px}
</style>
</head>
<body>

<header class="hero">
  <nav class="nav">
    <a class="brand" href="#">KELPORIA</a>
    <div class="menu">
      <a href="#">Startsida</a>
      <a href="#">Pris &amp; Funktioner</a>
      <a href="#">Om oss</a>
      <a href="#">Logga in</a>
      <a class="signup" href="#">Sign up</a>
    </div>
  </nav>
  <div class="hero-copy">
    <h1>Starta en gratis webshop.</h1>
    <p>Kelporia är en plattform där du enkelt skapar din egen webbutik. Kom igång på några minuter, helt utan kostnad, och börja sälja dina produkter redan idag.</p>
    <a class="btn-ghost" href="#">Skapa en webshop</a>
  </div>
  <div class="devices" role="img" aria-label="Webshoppen visad på surfplatta, mobil och bärbar dator"></div>
  <svg class="wave" viewBox="0 0 1200 200" preserveAspectRatio="none" aria-hidden="true">
    <path d="M0 90 C250 10 450 170 700 110 S1050 40 1200 80 V200 H0Z" fill="#ffffff" opacity=".25"/>
    <path d="M0 140 C300 70 500 200 800 140 S1100 90 1200 120 V200 H0Z" fill="#ffffff"/>
  </svg>
</header>

<section class="features">
  <div class="feature">
    <svg viewBox="0 0 40 40" fill="none" stroke="var(--blue)" stroke-width="2"><circle cx="20" cy="20" r="14"/><path d="M20 11v9l6 4"/></svg>
    <div><h3>Kort igång på 5 minuter</h3><p>Allt du behöver för att starta finns redan på plats. Välj ett tema, lägg till dina produkter och öppna din butik för kunderna direkt.</p></div>
  </div>
  <div class="feature">
    <svg viewBox="0 0 40 40" fill="none" stroke="var(--blue)" stroke-width="2"><path d="M4 8h6l4 18h18l4-12H12"/><circle cx="16" cy="32" r="2"/><circle cx="30" cy="32" r="2"/></svg>
    <div><h3>Skapa en gratis webbutik</h3><p>Det kostar ingenting att komma igång. Ingen startavgift, inga dolda kostnader och ingen bindningstid för dig som säljer.</p></div>
  </div>
  <div class="feature">
    <svg viewBox="0 0 40 40" fill="none" stroke="var(--blue)" stroke-width="2"><rect x="5" y="8" width="30" height="24" rx="2"/><path d="M5 14h30M11 20h18M11 26h12"/></svg>
    <div><h3>Intuitivt användargränssnitt</h3><p>Ett tydligt gränssnitt som gör det enkelt att hantera produkter, ordrar och kunder utan teknisk kunskap.</p></div>
  </div>
  <div class="feature">
    <svg viewBox="0 0 40 40" fill="none" stroke="var(--blue)" stroke-width="2"><circle cx="17" cy="17" r="10"/><path d="M25 25l10 10"/></svg>
    <div><h3>Sökmotoroptimerad</h3><p>Butiken är byggd för att synas i sökmotorer så att fler kunder hittar fram till dina produkter.</p></div>
  </div>
  <div class="feature">
    <svg viewBox="0 0 40 40" fill="none" stroke="var(--blue)" stroke-width="2"><path d="M4 8h6l4 18h18l4-12H12"/><circle cx="16" cy="32" r="2"/><circle cx="30" cy="32" r="2"/></svg>
    <div><h3>Designa din webshop</h3><p>Välj bland snygga teman och anpassa färger, typsnitt och layout så att butiken passar ditt varumärke.</p></div>
  </div>
  <div class="feature">
    <svg viewBox="0 0 40 40" fill="none" stroke="var(--blue)" stroke-width="2"><rect x="7" y="5" width="26" height="30" rx="2"/><path d="M13 13h14M13 19h14M13 25h9"/></svg>
    <div><h3>Smart Dashboard</h3><p>Följ försäljning och besökare i realtid med en översikt som ger dig full kontroll över butiken.</p></div>
  </div>
</section>

<section class="intro">
  <h2>Funktioner</h2>
  <p>Följande är några av Kelporias nyckelfunktioner. Välj det paket som passar dig bäst och uppgradera när du vill.</p>
  <p>Du kan när som helst byta paket och alla dina produkter, ordrar och inställningar följer med utan problem.</p>
</section>

<section class="plans">
  <article class="plan">
    <div class="tag">STANDARDPAKETET</div>
    <div class="price">Gratis</div>
    <ul><li>Obegränsat antal produkter</li><li>Egen webbadress</li><li>Säker betalning</li><li>Statistik och rapporter</li><li>Support via e-post</li></ul>
    <svg class="plan-wave" viewBox="0 0 300 150" preserveAspectRatio="none" aria-hidden="true">
      <path d="M0 50 C80 0 150 90 300 30 V150 H0Z" fill="var(--blue-light)"/>
      <path d="M0 80 C90 40 180 120 300 70 V150 H0Z" fill="var(--blue)"/>
    </svg>
    <a class="buy" href="#">Purchase</a>
  </article>
  <article class="plan">
    <div class="tag">PREMIUMPAKETET</div>
    <div class="price">149<small>kr / mån</small></div>
    <ul><li>Allt i Standard</li><li>Eget domännamn</li><li>Avancerade teman</li><li>Rabattkoder</li><li>Prioriterad support</li></ul>
    <svg class="plan-wave" viewBox="0 0 300 150" preserveAspectRatio="none" aria-hidden="true">
      <path d="M0 50 C80 0 150 90 300 30 V150 H0Z" fill="var(--blue-light)"/>
      <path d="M0 80 C90 40 180 120 300 70 V150 H0Z" fill="var(--blue)"/>
    </svg>
    <a class="buy" href="#">Purchase</a>
  </article>
</section>

<section class="small-features">
  <div class="small"><h4>Small Feature</h4><p>Hantera lager och varianter på ett enkelt sätt. Håll koll på vad som finns kvar och få en påminnelse när det är dags att fylla på.</p></div>
  <div class="small"><h4>Small Feature</h4><p>Ta emot betalningar med kort och faktura. Alla transaktioner hanteras säkert och pengarna når ditt konto snabbt.</p></div>
  <div class="small"><h4>Small Feature</h4><p>Skicka orderbekräftelser automatiskt till kunderna och håll dem uppdaterade genom hela leveransen.</p></div>
  <div class="small"><h4>Small Feature</h4><p>Butiken fungerar lika bra i mobilen som på datorn, så att dina kunder kan handla var de än befinner sig.</p></div>
  <div class="small"><h4>Small Feature</h4><p>Skapa kampanjer och rabattkoder för att locka nya kunder och belöna dem som kommer tillbaka.</p></div>
  <div class="small"><h4>Small Feature</h4><p>Exportera ordrar och kunddata när du vill och koppla ihop butiken med ditt bokföringssystem.</p></div>
</section>

<footer class="footer">
  <div>
    <div class="brand">KELPORIA</div>
    <p>Kelporia är en molnbaserad plattform för e-handel som hjälper dig att starta och driva en egen webbutik.</p>
  </div>
  <div>
    <h5>Support</h5>
    <ul><li>Om oss</li><li>Tjänster</li><li>Priser</li><li>Vanliga frågor</li><li>Blogg</li></ul>
  </div>
  <div>
    <h5>Chirpline Feeds</h5>
    <div class="tweet"><i></i><p>@kelporia Nytt tema släppt idag, perfekt för dig som säljer kläder och accessoarer.</p></div>
    <div class="tweet"><i></i><p>@kelporia Vi har uppdaterat dashboarden med ny statistik.</p></div>
  </div>
  <div>
    <h5>Contact Us</h5>
    <ul class="contact"><li><i></i>Storgatan 12, 111 22 Stockholm</li><li><i></i>08-555 010 20</li><li><i></i>hej@kelporia.example</li></ul>
  </div>
</footer>

</body>
</html>
```